Bryncarn foot health or foot health bryncarn

Treatments in comfort of your own home
Delia Marsh cert KTLFr Pod, BGNVect
Treatments will be listed on the leaflet I will attach
I am a Foot Health practitioner,
I want to mention I do home visits throughout Pembrokeshire & Ceredigion.
Tel. 07730915264
I have 2 logs to forward to you they are the associations I belong to .
One of which is also a certification mark. It is important that the same colour is used for this mark. They are not the main focus, they are just recognised mark. To be at the top or bottom of the page.
There is a local business called Glenmorrow foot clinic, so my business has to be bryncarn foot health, or foot health bryncarn
soon I will also need a web page and cards designed, so please keep this in mind when designing the Artwork. I will also need an email on the leaflet but I will wait and see what the design is first before I confirm it as I have several.
I hope this is enough info for you.
Many thanks,
Delia Marsh

Target Market(s)

Mostly the elderly, some middle age women, but it is a service for all ages. The elderly are my main clients.

Industry/Entity Type

Health

Font styles to use
Serif
Sans Serif

Colors

Designer to choose colors to be used in the design.

Requirements
Must have
• Covering Pembrokeshire & Ceredigion.
Treatments include:- as listed on example leaflet I sent
Phone number a size that's easily readable.
I am open to colours. I love bright colours, but also like the more conservative colours as long as it looks professional. I'm wanting it to look more up market.
Nice to have
• Logo for Covenant and KTS logo obviously smaller, but also recognisable and either at the top of page or bottom. These are not to be main focal point.

```html
<!DOCTYPE html>
<html lang="en">
<head>
<meta charset="utf-8">
<title>Foot Health Bryncarn – Comprehensive Foot Care</title>
<link rel="stylesheet" href="https://fonts.googleapis.com/css2?family=Gelasio:wght@400&family=Sorts+Mill+Goudy&display=swap">
<style>
  :root {
    --ink: #2e5b55;
    --accent: #3c8276;
    --band: #e1f1e8;
    --mark-soft: #cfe7da;
    --mark-fill: #7fa49b;
    --badge: #1f5a3c;
    --badge-ring: #c9a640;
    --paper: #ffffff;
  }
  html, body {
    margin: 0;
    padding: 0;
    width: 856px;
    height: 1200px;
    overflow: hidden;
    background: var(--paper);
  }
  .leaflet {
    position: relative;
    width: 856px;
    height: 1200px;
    color: var(--ink);
    font-family: "Sorts Mill Goudy", Georgia, serif;
  }
  .brand-mark {
    position: absolute;
    left: 78px;
    top: 52px;
  }
  .brand-name {
    position: absolute;
    left: 314px;
    top: 58px;
    margin: 0;
    font-family: "Gelasio", Georgia, serif;
    font-weight: 400;
    color: var(--ink);
    line-height: 1;
  }
  .brand-name .line-1 { display: block; font-size: 90px; letter-spacing: 0.5px; }
  .brand-name .line-2 { display: block; font-size: 66px; margin-top: 4px; }
  .band {
    position: absolute;
    left: 44px;
    width: 759px;
    background: var(--band);
    color: var(--accent);
    text-align: center;
    font-variant: small-caps;
    letter-spacing: 1.5px;
    margin: 0;
    font-weight: 400;
  }
  .band-services { top: 258px; height: 69px; line-height: 69px; font-size: 40px; }
  .band-treatments { top: 427px; height: 69px; line-height: 69px; font-size: 40px; }
  .band-coverage {
    top: 822px; height: 113px; font-size: 40px;
    display: flex; flex-direction: column; justify-content: center; line-height: 1.12;
  }
  .practitioner {
    position: absolute;
    top: 346px;
    left: 0;
    width: 847px;
    margin: 0;
    text-align: center;
    font-size: 33px;
    letter-spacing: 1px;
  }
  .treatment-list {
    position: absolute;
    top: 512px;
    left: 0;
    width: 847px;
    margin: 0;
    padding: 0;
    list-style: none;
    text-align: center;
    font-size: 33px;
    line-height: 46.8px;
    letter-spacing: 1px;
  }
  .contact {
    position: absolute;
    left: 73px;
    top: 942px;
    font-size: 33px;
    letter-spacing: 1.5px;
    line-height: 42px;
  }
  .contact p { margin: 0; }
  .contact .phone { font-size: 39px; margin-top: 12px; letter-spacing: 1px; }
  .contact .email { font-size: 23px; margin-top: 24px; letter-spacing: 1px; }
  .association-badge {
    position: absolute;
    left: 660px;
    top: 1014px;
  }
</style>
</head>
<body>
<main class="leaflet">
  <svg class="brand-mark" width="180" height="180" viewBox="0 0 180 180" aria-hidden="true">
    <circle cx="90" cy="90" r="86" fill="var(--mark-soft)"/>
  </svg>
  <h1 class="brand-name">
    <span class="line-1">Foot Health</span>
    <span class="line-2">Bryncarn</span>
  </h1>

  <h2 class="band band-services">Comprehensive Foot Care</h2>
  <p class="practitioner">Delia Marsh, KTLFr Pod, BGNVect</p>

  <h2 class="band band-treatments">Treatments Include:</h2>
  <ul class="treatment-list">
    <li>Diabetic Foot Care</li>
    <li>Ingrowing Toenails</li>
    <li>Corn &amp; Callous Treatment</li>
    <li>Toenail Clipping</li>
    <li>Fungal Infection Treatment</li>
    <li>Cracked Heels</li>
  </ul>

  <h2 class="band band-coverage">
    <span>Home visits throughout</span>
    <span>Pembrokeshire &amp; Ceredigion</span>
  </h2>

  <section class="contact">
    <p>Care in the comfort of your own home.</p>
    <p>Call to make an arrangement.</p>
    <p class="phone">Tel. 07730 915264</p>
    <p class="email">E-mail ____________@____________</p>
  </section>

  <svg class="association-badge" width="150" height="150" viewBox="0 0 150 150" role="img" aria-label="Covenant association membership badge">
    <circle cx="75" cy="75" r="72" fill="var(--badge)"/>
  </svg>
</main>
</body>
</html>
```